beauty salon

providing waxing services from a home base this must include which I will provide a price list and an address

Industry/Entity Type

Beauty Salon

Font styles to use
Script

Colors

Designer to choose colors to be used in the design.

```html
<!DOCTYPE html>
<html lang="en">
<head>
<meta charset="utf-8">
<title>Maren's Willow Studio – Price List</title>
<link href="https://fonts.googleapis.com/css2?family=Arvo:wght@700&family=Pompiere&family=Arimo:wght@400;700&family=Tinos:ital,wght@1,700&family=Playball&display=swap" rel="stylesheet">
<style>
  :root {
    --sea: #3bb4c7;
    --edge: #52bdd0;
    --frame-red: #d8343a;
    --title-yellow: #ffff00;
    --band-mint: #92d2c6;
    --ink: #1c2530;
    --row-light: #86d2de;
    --row-dark: #66c4d3;
    --white: #ffffff;
    --badge-red: #d8251f;
    --badge-rim: #f7b7c0;
    --badge-purple: #8e1f78;
  }
  * { box-sizing: border-box; margin: 0; padding: 0; }
  html, body { width: 851px; height: 1200px; overflow: hidden; background: var(--edge); }
  .flyer {
    position: relative; width: 851px; height: 1200px; overflow: hidden;
    background: var(--sea);
    font-family: "Arimo", Arial, sans-serif; color: var(--ink);
  }
  .flyer__frame {
    position: absolute; left: 9px; top: 8px; right: 9px; bottom: 8px;
    border: 4px solid var(--frame-red);
  }
  .hero-art {
    position: absolute; left: 80px; top: 38px; width: 690px; height: 160px;
    border-radius: 80px;
    background: radial-gradient(ellipse at 50% 55%, rgba(210,245,240,.5), rgba(255,255,255,.1) 55%, rgba(255,255,255,0) 75%);
  }
  .silhouette {
    position: absolute; border-radius: 140px 140px 60px 60px;
    background: rgba(255,255,255,.1);
  }
  .silhouette--lady { left: 100px; top: 420px; width: 300px; height: 450px; }
  .silhouette--man  { left: 450px; top: 480px; width: 300px; height: 400px; }
  .salon-name {
    position: absolute; left: 0; right: 0; top: 200px;
    text-align: center; font-family: "Arvo", "Rockwell", serif; font-weight: 700;
    font-size: 62px; color: var(--title-yellow); letter-spacing: .5px; white-space: nowrap;
  }
  .therapist {
    position: absolute; left: 67px; top: 283px; width: 714px; height: 52px;
    background: var(--band-mint);
    display: flex; align-items: center; justify-content: center; gap: 6px;
    font-size: 19px; padding-top: 6px; white-space: nowrap;
  }
  .therapist__name { font-family: "Tinos", "Times New Roman", serif; font-style: italic; font-weight: 700; font-size: 37px; margin-top: -8px; }
  .section-title {
    position: absolute; font-family: "Pompiere", "Arial Narrow", sans-serif;
    font-size: 52px; font-weight: 400; color: var(--ink); line-height: 1;
    transform: scaleX(.78); transform-origin: left center; white-space: nowrap;
  }
  .section-title--lady { left: 90px; top: 356px; }
  .section-title--men { left: 483px; top: 356px; }
  .section-title--eye { left: 460px; top: 816px; transform: scaleX(.86); }
  .price-list { position: absolute; list-style: none; }
  .price-list li {
    height: 35.6px; display: flex; align-items: center; font-size: 20px;
    background: var(--row-light);
  }
  .price-list li:nth-child(even) { background: var(--row-dark); }
  .price-list .item { width: 245px; padding-left: 31px; }
  .price-list--lady { left: 70px; top: 417px; width: 338px; }
  .price-list--men { left: 443px; top: 417px; width: 338px; }
  .price-list--eye { left: 443px; top: 881px; width: 338px; }
  .price-list--eye .item { width: 243px; padding-left: 28px; }
  .info-card {
    position: absolute; top: 1036px; height: 116px; font-size: 18px;
    letter-spacing: .6px;
  }
  .info-card--contact {
    left: 42px; width: 266px; padding: 20px 0 0 32px; line-height: 24px; font-style: normal;
    background: linear-gradient(90deg, rgba(255,255,255,.1), var(--white) 70%);
    border-radius: 0 30px 30px 0;
  }
  .info-card--hours {
    left: 515px; width: 286px; padding: 20px 0 0 20px; line-height: 26px;
    background: linear-gradient(90deg, var(--white) 45%, rgba(255,255,255,.1));
    border-radius: 30px 0 0 30px;
  }
  .hours { display: grid; grid-template-columns: 128px auto; }
  .hours-title {
    position: absolute; left: 548px; top: 1014px;
    font-family: "Playball", cursive; font-size: 30px; font-weight: 400; color: #111;
  }
  .offer { position: absolute; left: 295px; top: 960px; width: 210px; height: 215px; }
  .offer svg { position: absolute; left: 0; top: 0; }
  .offer__pct {
    position: absolute; left: 10px; top: 36px; width: 90px; text-align: center;
    color: var(--white); font-weight: 700; font-size: 32px; line-height: 40px;
  }
  .offer__pct sup { font-size: 16px; }
  .offer__text {
    position: absolute; left: 50px; top: 104px; width: 140px; text-align: center;
    color: var(--white); font-weight: 700; font-size: 16px; line-height: 22px;
  }
</style>
</head>
<body>
<main class="flyer">
  <div class="flyer__frame"></div>
  <div class="hero-art" role="img" aria-label="Sparkle swirl with line illustration of two figures sitting on stools"></div>
  <div class="silhouette silhouette--lady" role="img" aria-label="Faint silhouette of a woman's head in profile"></div>
  <div class="silhouette silhouette--man" role="img" aria-label="Faint silhouette of a man's head in profile"></div>

  <h1 class="salon-name">Maren's Willow Studio</h1>
  <p class="therapist">Beauty Therapist: <span class="therapist__name">Maren</span> Diploma of Beauty Therapy at Arden Vale College</p>

  <h2 class="section-title section-title--lady">Lady's Waxing</h2>
  <ul class="price-list price-list--lady">
    <li><span class="item">Eyebrow</span><span>$8</span></li>
    <li><span class="item">Upper lip</span><span>$8</span></li>
    <li><span class="item">Chin</span><span>$8</span></li>
    <li><span class="item">Face wax</span><span>$25</span></li>
    <li><span class="item">Bikini line</span><span>$15</span></li>
    <li><span class="item">G string</span><span>$20</span></li>
    <li><span class="item">½ Brazilian</span><span>$30</span></li>
    <li><span class="item">Full Brazilian</span><span>$40</span></li>
    <li><span class="item">Half arm</span><span>$20</span></li>
    <li><span class="item">Upper half arm</span><span>$20</span></li>
    <li><span class="item">Full arm</span><span>$25</span></li>
    <li><span class="item">Half leg</span><span>$15</span></li>
    <li><span class="item">Upper leg</span><span>$20</span></li>
    <li><span class="item">¾ Leg</span><span>$25</span></li>
    <li><span class="item">Full leg</span><span>$35</span></li>
  </ul>

  <h2 class="section-title section-title--men">Men's Waxing</h2>
  <ul class="price-list price-list--men">
    <li><span class="item">Eyebrow</span><span>$10</span></li>
    <li><span class="item">Half arm</span><span>$20</span></li>
    <li><span class="item">Upper half arm</span><span>$25</span></li>
    <li><span class="item">Full arm</span><span>$30</span></li>
    <li><span class="item">Half leg</span><span>$25</span></li>
    <li><span class="item">Full leg</span><span>$45</span></li>
    <li><span class="item">Chest wax</span><span>$40</span></li>
    <li><span class="item">Back wax</span><span>$35</span></li>
    <li></li>
  </ul>

  <h2 class="section-title section-title--eye">Eye Enhancement</h2>
  <ul class="price-list price-list--eye">
    <li><span class="item">Eyebrow tint</span><span>$12</span></li>
    <li><span class="item">Eyelash tint</span><span>$15</span></li>
  </ul>

  <address class="info-card info-card--contact">
    12 Finch Lane<br>Willow Heights<br>Mobile: 0400 555 182
  </address>

  <section class="info-card info-card--hours">
    <div class="hours">
      <span>Wednesday:</span><span>10am - 4pm</span>
      <span>Fridays:</span><span>10am - 7pm</span>
      <span>Saturday:</span><span>10am - 4pm</span>
    </div>
  </section>
  <h3 class="hours-title">Time</h3>

  <div class="offer">
    <svg width="210" height="215" viewBox="0 0 210 215" aria-hidden="true">
      <path d="M120 66 C165 66 193 98 193 135 C193 175 160 204 120 204 C80 204 48 175 48 135 C48 110 60 90 80 78 L66 58 Z" fill="var(--badge-red)" stroke="var(--badge-rim)" stroke-width="5"/>
      <circle cx="55" cy="55" r="45" fill="var(--badge-purple)" stroke="var(--white)" stroke-width="4"/>
    </svg>
    <div class="offer__pct">10<sup>%</sup></div>
    <div class="offer__text">DISCOUNT<br>ON FIRST<br>TREATMENT</div>
  </div>
</main>
</body>
</html>
```